FERNLOOP Guiding Answers Across The Digital Frontier\Government Contracting IT, Software, Networks

We need a business card design for a new Government Joint Venture based out of Omaha, NE. We provide all types of technology needs to all types of Government agencies. I have attached logo and capability statement to identify our companies industry and offerings. extremely import information that needs to be identified on the cards is SBA: 8(a), SBA: SDB, SBA: HUBZone

Target Market(s)

Government Contracting Officers

Industry/Entity Type

Business

Contact Information for Business Card

Delia Frost
Vice President
7281 W 48th Avenue
Omaha, NE 68342
P: 402-555-3172
F: 402-555-3173
Toll: 855-555-2046
delia@fernloop.co
http://www.fernloop.co
Gideon Vally
President
7281 W 48th Avenue
Omaha, NE 68342
P: 402-555-3172
F: 402-555-3173
Toll: 855-555-2046
gideon@fernloop.co
http://www.fernloop.co

Number of Pages Required

4 page

Font styles to use
Serif

Requirements
Must have
• Look and feel should be technical.

```html
<!DOCTYPE html>
<html lang="en">
<head>
<meta charset="utf-8">
<title>Fernloop Business Card</title>
<link href="https://fonts.googleapis.com/css2?family=Roboto+Slab:wght@300;400;700&display=swap" rel="stylesheet">
<style>
  :root {
    --stage: #e9e8ec;
    --violet: #3b1fd0;
    --violet-deep: #23108f;
    --violet-mid: #3218b8;
    --paper: #ffffff;
    --paper-shade: #eceaf2;
    --ink-light: #ffffff;
    --ink-soft: #e4defb;
  }
  html, body {
    margin: 0;
    padding: 0;
    width: 1200px;
    height: 871px;
    overflow: hidden;
    background: var(--stage);
    font-family: "Roboto Slab", Georgia, serif;
  }
  .canvas {
    position: relative;
    width: 1200px;
    height: 871px;
  }
  .card {
    position: absolute;
    width: 600px;
    height: 343px;
    box-shadow: 0 10px 28px rgba(20, 10, 60, 0.28);
    overflow: hidden;
  }
  /* Back of card */
  .card-back {
    left: 90px;
    top: 70px;
    background: linear-gradient(135deg, var(--violet) 0%, var(--violet-mid) 55%, var(--violet-deep) 100%);
    display: flex;
    flex-direction: column;
    align-items: center;
    justify-content: center;
    gap: 22px;
  }
  .brand {
    display: flex;
    align-items: center;
    gap: 12px;
    font-weight: 700;
    letter-spacing: 3px;
    white-space: nowrap;
  }
  .brand-dot {
    border-radius: 50%;
    flex: none;
  }
  .card-back .brand { color: var(--ink-light); font-size: 38px; }
  .card-back .brand-dot { width: 32px; height: 32px; background: var(--ink-light); }
  .back-web {
    color: var(--ink-soft);
    font-size: 14px;
    letter-spacing: 2px;
    font-weight: 300;
  }
  /* Front of card */
  .card-front {
    left: 510px;
    top: 460px;
    background: linear-gradient(160deg, var(--paper) 30%, var(--paper-shade) 100%);
  }
  .front-brand {
    position: absolute;
    left: 28px;
    top: 0;
    height: 100%;
    width: 270px;
    display: flex;
    flex-direction: column;
    justify-content: center;
    gap: 14px;
  }
  .card-front .brand { color: var(--violet); font-size: 31px; letter-spacing: 2px; }
  .card-front .brand-dot { width: 28px; height: 28px; background: var(--violet); }
  .certifications {
    margin: 0;
    padding-left: 40px;
    font-size: 10.5px;
    font-weight: 400;
    line-height: 16px;
    color: var(--violet-mid);
    letter-spacing: 0.3px;
  }
  .contact-panel {
    position: absolute;
    left: 318px;
    top: 48px;
    width: 282px;
    height: 258px;
    border-radius: 16px 0 0 16px;
    background: linear-gradient(150deg, var(--violet) 0%, var(--violet-mid) 60%, var(--violet-deep) 100%);
    color: var(--ink-light);
    padding: 20px 12px 0 22px;
    box-sizing: border-box;
  }
  .person-name {
    margin: 0;
    font-size: 20px;
    font-weight: 700;
    letter-spacing: 0.5px;
  }
  .person-title {
    margin: 4px 0 16px;
    font-size: 13px;
    font-weight: 300;
    color: var(--ink-soft);
  }
  .address {
    margin: 0 0 12px;
    font-size: 11px;
    font-weight: 300;
    white-space: nowrap;
  }
  .contact-list {
    list-style: none;
    margin: 0;
    padding: 0;
  }
  .contact-list li {
    display: flex;
    align-items: center;
    gap: 12px;
    font-size: 12.5px;
    font-weight: 400;
    line-height: 22px;
    white-space: nowrap;
  }
  .contact-list svg {
    width: 13px;
    height: 13px;
    flex: none;
  }
  .contact-list .email { font-size: 11.5px; font-weight: 300; }
</style>
</head>
<body>
<main class="canvas">

  <section class="card card-back" aria-label="Card back">
    <div class="brand"><span class="brand-dot"></span>FERNLOOP</div>
    <div class="back-web">www.fernloop.com</div>
  </section>

  <section class="card card-front" aria-label="Card front">
    <div class="front-brand">
      <div class="brand"><span class="brand-dot"></span>FERNLOOP</div>
      <p class="certifications">SBA: 8(a) &nbsp;|&nbsp; SBA: SDB<br>SBA: HUBZone</p>
    </div>

    <div class="contact-panel">
      <h1 class="person-name">Delia Frost</h1>
      <p class="person-title">Vice President</p>
      <p class="address">7281 W 48th Avenue Omaha, NE 68342</p>
      <ul class="contact-list">
        <li>
          <svg viewBox="0 0 16 16" fill="currentColor"><path d="M2 6c0-2 2-3 6-3s6 1 6 3l-2 1-1-2H5L4 7 2 6zM4 8h8l1 5H3z"/></svg>
          402-555-3172
        </li>
        <li>
          <svg viewBox="0 0 16 16" fill="currentColor"><rect x="4" y="1" width="8" height="5"/><rect x="1" y="6" width="14" height="7" rx="1"/><rect x="4" y="10" width="8" height="5" fill="#2a14a8"/></svg>
          402-555-3173
        </li>
        <li>
          <svg viewBox="0 0 16 16" fill="currentColor"><path d="M2 6c0-2 2-3 6-3s6 1 6 3l-2 1-1-2H5L4 7 2 6zM4 8h8l1 5H3z"/></svg>
          855-555-2046&nbsp;&nbsp;Toll Free
        </li>
        <li class="email">
          <svg viewBox="0 0 16 16" fill="none" stroke="currentColor" stroke-width="1.5"><rect x="1.5" y="3.5" width="13" height="9"/><path d="M1.5 3.5 8 9l6.5-5.5"/></svg>
          delia@fernloop.co
        </li>
      </ul>
    </div>
  </section>

</main>
</body>
</html>
```